Quorlick`s Maintenance website
Tagline(Proffesionally done for less than the rest)
Project: Quorlick`s Maintenance website
Quorlick`s Maintenance website - Cleaning
Creative Brief
Cleaning
www.QUORLICK`S-example.com

```html
<!DOCTYPE html>
<html lang="en">
<head>
<meta charset="utf-8">
<title>Quorlick`s Maintenance LLC</title>
<link href="https://fonts.googleapis.com/css2?family=Arimo:wght@400;700&family=PT+Sans:wght@400;700&family=PT+Serif&display=swap" rel="stylesheet">
<style>
:root{
  --navy:#0d3f73;
  --orange:#f7931e;
  --orange-deep:#e06d0c;
  --orange-text:#f47c11;
  --blue-accent:#1b8fd8;
  --page:#f4f3f3;
  --ink:#2a2a2a;
  --black:#0b0b0b;
}
*{box-sizing:border-box;margin:0;padding:0}
html,body{width:988px;height:1200px;overflow:hidden}
body{background:var(--navy);font-family:"Arimo",Arial,sans-serif;color:var(--ink);position:relative}
.footer-band{position:absolute;left:0;top:1113px;width:988px;height:87px;background:linear-gradient(90deg,var(--orange-deep),var(--orange) 50%,var(--orange-deep))}
.page{position:absolute;left:120px;top:0;width:748px;height:1138px;background:var(--page);border-radius:0 0 6px 6px;box-shadow:0 0 6px rgba(0,0,0,.25)}
.abs{position:absolute}

.top-links{right:13px;top:6px;font-size:8.5px;color:#222;display:flex;gap:4px;align-items:center}
.flags{display:flex;gap:3px;margin-left:4px}
.flag{width:16px;height:11px;border:1px solid #ccc}
.flag.fr{background:linear-gradient(90deg,#1c3f9e 33%,#fff 33% 66%,#d22 66%)}
.flag.uk{background:#1c3f9e}
.flag.us{background:repeating-linear-gradient(#c22 0 1.5px,#fff 1.5px 3px)}

.brand{left:20px;top:30px;display:flex;align-items:center;gap:8px}
.brand-mark{width:22px;height:22px;border-radius:50%;background:var(--orange)}
.brand-name{font-family:"PT Sans",sans-serif;font-weight:700;font-size:30px;color:var(--navy);letter-spacing:.5px}
.brand-sub{left:50px;top:68px;font-family:"PT Sans",sans-serif;font-weight:700;font-size:10px;color:var(--navy);letter-spacing:1px}

.cta{right:13px;top:74px;font-family:"PT Sans",sans-serif;font-size:13px;color:var(--navy);display:flex;align-items:baseline;gap:4px}
.cta b{font-size:15px}
.cta .free{color:var(--orange);font-weight:700;font-size:18px}

.nav{left:-14px;top:96px;width:777px;height:41px;background:var(--orange);display:flex;align-items:center;padding-left:8px}
.nav::before,.nav::after{content:"";position:absolute;top:41px;border-top:12px solid #c96a10}
.nav::before{left:0;border-right:12px solid transparent}
.nav::after{right:0;border-left:12px solid transparent}
.nav a{font-family:"PT Serif",serif;font-size:13px;color:#fff;text-decoration:none;padding:0 8px;border-right:1px solid rgba(255,255,255,.45);line-height:30px}
.nav a:last-child{border-right:none}

.slider{left:0;top:137px;width:748px;height:303px;background:linear-gradient(180deg,#2a5fc0 0%,#3f6fb0 45%,#7b6a66 75%,#2b2a33 100%)}
.slide-arrow{top:279px;width:37px;height:37px;background:var(--black);border-radius:4px}
.slide-arrow svg{width:37px;height:37px}
.caption-bar{left:0;top:440px;width:748px;height:34px;background:var(--black)}
.dots{left:12px;top:10px;display:flex;gap:5px}
.dot{width:14px;height:14px;border-radius:50%;border:2px solid #fff;background:var(--orange)}
.dot.on{background:var(--blue-accent)}
.tagline{right:13px;top:5px;font-family:"PT Sans",sans-serif;font-size:18px;color:var(--orange)}
.tagline .done{color:var(--blue-accent);font-weight:700;margin:0 6px}
.tagline .rest{color:var(--blue-accent)}

.dropdown{left:274px;top:137px;width:137px;background:var(--orange);padding:2px 0}
.dropdown li{list-style:none;font-size:11px;color:#fff;padding:0 10px;line-height:21px}
.dropdown li.active{background:var(--navy)}

h2{font-family:"PT Sans",sans-serif;font-weight:400;font-size:15px;color:#111}
h2 span{color:var(--orange-text)}
.welcome-title{left:15px;top:490px}
.welcome-title span{font-size:19px}
.rule{border-bottom:1px dotted #888}
.intro-photo{left:17px;top:525px;width:145px;height:114px;border:3px solid #c9ccd1;background:linear-gradient(135deg,#123a66,#4a8fc0 60%,#1b4e80)}
.body-copy{font-size:8.6px;line-height:11.7px;text-align:justify;color:#333;hyphens:auto}
.intro-text{left:172px;top:526px;width:335px;height:118px;overflow:hidden}
.intro-cont{left:15px;top:648px;width:492px}

.extra-title{left:20px;top:766px}
.checks{left:24px;top:811px;display:grid;grid-template-columns:143px 162px 175px;row-gap:9px}
.checks li{list-style:none;font-size:9.8px;color:#222;display:flex;align-items:center;gap:8px;height:16px}
.checks svg{width:14px;height:14px}

.gallery-tab{left:50px;top:908px;width:112px;height:23px;background:var(--orange);color:#fff;font-family:"PT Sans",sans-serif;font-size:14px;padding-left:11px;line-height:23px}
.gallery{left:34px;top:931px;width:460px;height:98px;background:linear-gradient(#fdfdfd,#dcdcdc);border:1px solid #c9c9c9}
.thumb{top:15px;width:129px;height:72px;border:1px solid #fff}
.g-arrow{width:26px;height:26px;background:var(--black);border-radius:3px}
.g-arrow svg{width:26px;height:26px}

.certified{left:37px;top:1062px;width:206px;text-align:center;font-family:"PT Sans",sans-serif;font-size:17px;line-height:22px;color:#111}
.certified span{color:var(--orange-text)}
.badge{top:1049px;width:62px;height:62px;border-radius:50%}

.card{left:529px;width:201px;background:#fff;border:2px solid #cfcfcf;box-shadow:0 3px 4px rgba(0,0,0,.15)}
.card-photo{height:80px}
.card-ribbon{position:relative;margin:0 -8px;height:30px;background:linear-gradient(#f49a2c,var(--orange-deep));color:#fff;text-align:center;font-family:"PT Sans",sans-serif;font-size:15px;line-height:30px}
.card-ribbon::before,.card-ribbon::after{content:"";position:absolute;top:30px;border-top:7px solid #a64f08}
.card-ribbon::before{left:0;border-left:7px solid transparent}
.card-ribbon::after{right:0;border-right:7px solid transparent}
.card-body{padding:10px 10px 0;font-size:8.8px;line-height:12px;color:#555;text-align:justify;height:62px;overflow:hidden}
.card-body.contact{padding-top:8px;line-height:10.8px;text-align:left;font-size:8.8px;height:66px}
.card-body .name{font-size:12.5px;line-height:15px;color:#333}
.card-foot{display:flex}
.card-more{margin-left:auto;width:68px;height:18px;background:var(--navy);color:#fff;font-size:9.5px;line-height:18px;text-align:center;border-radius:6px 0 0 0}

.footer-info{left:132px;top:1146px;font-size:10.5px;line-height:16px;color:#fff}
.follow{right:133px;top:1146px;display:flex;gap:4px;align-items:center;color:#fff;font-size:12px}
.follow i{width:17px;height:17px;border-radius:50%;background:#fff;display:inline-block;opacity:.9}
.follow i:first-of-type{margin-left:6px}
.copyright{right:133px;top:1180px;font-size:10px;color:#fff}
</style>
</head>
<body>
<div class="footer-band"></div>

<div class="page">
  <div class="abs top-links">Home | Our Mission | Our Promise | Awnings
    <span class="flags"><span class="flag fr"></span><span class="flag uk"></span><span class="flag us"></span></span>
  </div>

  <div class="abs brand"><span class="brand-mark"></span><span class="brand-name">QUORLICK`S</span></div>
  <div class="abs brand-sub">MAINTENANCE LLC</div>

  <div class="abs cta">
    <svg width="12" height="16" viewBox="0 0 12 16"><path d="M3 1 L6 4 L4 6 Q5 10 8 12 L10 10 L12 13 L9 15 Q2 12 1 3 Z" fill="#f7931e"/></svg>
    <b>Contact Us</b> to Schedule <span class="free">FREE</span> Consultation
  </div>

  <nav class="abs nav">
    <a>Home</a><a>Window Washing</a><a>Water Fed Poles</a><a>Pressure Washing</a><a>Gutters</a><a>Our Company</a><a>Discounts</a><a>Pricing</a><a>Contact Us</a>
  </nav>

  <div class="abs slider" role="img" aria-label="City skyline at dusk with tall office towers and a clock tower"></div>
  <div class="abs slide-arrow" style="left:-8px"><svg viewBox="0 0 37 37"><path d="M22 10 L13 18.5 L22 27" stroke="#fff" stroke-width="4" fill="none"/></svg></div>
  <div class="abs slide-arrow" style="right:-8px"><svg viewBox="0 0 37 37"><path d="M15 10 L24 18.5 L15 27" stroke="#fff" stroke-width="4" fill="none"/></svg></div>

  <ul class="abs dropdown">
    <li>Restaurants</li><li class="active">Bank Drive Thru's</li><li>Fast Food Drive Thru's</li><li>House Gutters</li><li>Mobile Homes</li>
  </ul>

  <div class="abs caption-bar">
    <div class="abs dots"><span class="dot on"></span><span class="dot"></span><span class="dot"></span><span class="dot"></span></div>
    <div class="abs tagline">Proffesionally<span class="done">DONE</span>for less than <span class="rest">the Rest</span></div>
  </div>

  <h2 class="abs welcome-title">Welcome to <span>Quorlick`s Maintenance LLC</span></h2>
  <div class="abs rule" style="left:15px;top:516px;width:492px"></div>
  <div class="abs intro-photo" role="img" aria-label="Window squeegee on a glass pane"></div>
  <p class="abs body-copy intro-text" lang="en">Thank you for visiting our website. Quorlick`s Maintenance LLC understands that sometimes building maintenance often falls at the bottom of your to-do list. We also understand the importance and impact that cleaning can have in the appearance of your business or home. If you are looking for a professional and reliable maintenance company that is located in the state of Pensilvania you have come to the right place. We are a locally owned business offering our services all year-round for both commercial and residential customers. When you choose Quorlick`s Maintenance LLC, you will receive prompt and professional service at an affordable rate. Please take a tour of our website and while you're here, request a free estimate and find out just how affordable our services can</p>
  <p class="abs body-copy intro-cont" lang="en">be service at an affordable rate. Please take a tour of our website and while you're here, request a free estimate and find out just how affordable our services can be. We can completely customize a cleaning package and schedule to fit not only your needs, but your budget as well. No job is too big or too small for us to handle. Our basic window cleaning includes cleaning the windows, detailing the edges of the windows, and wiping down the frames. However, we do offer a wide range of additional services that go hand-in-hand with window cleaning. We can completely customize a cleaning package and schedule to fit not only your needs, but your budget as well. No job is too big or too small for us to handle. Our basic window cleaning includes cleaning the windows, detailing the edges of the windows, and wiping down the frames. However, we do offer a wide range of additional services that go hand-in-hand with window cleaning. Those additional cleaning services are listed below.</p>

  <h2 class="abs extra-title">Additonal <span>Cleaning Services:</span></h2>
  <div class="abs rule" style="left:20px;top:790px;width:480px"></div>
  <ul class="abs checks">
    <li><svg viewBox="0 0 14 14"><path d="M2 7 L6 11 L12 2" stroke="#666" stroke-width="2" fill="none"/></svg>Skylights</li>
    <li><svg viewBox="0 0 14 14"><path d="M2 7 L6 11 L12 2" stroke="#666" stroke-width="2" fill="none"/></svg>Hard Water Removal</li>
    <li><svg viewBox="0 0 14 14"><path d="M2 7 L6 11 L12 2" stroke="#666" stroke-width="2" fill="none"/></svg>Light Fixtures &amp; Chandeliers</li>
    <li><svg viewBox="0 0 14 14"><path d="M2 7 L6 11 L12 2" stroke="#666" stroke-width="2" fill="none"/></svg>Solar panel</li>
    <li><svg viewBox="0 0 14 14"><path d="M2 7 L6 11 L12 2" stroke="#666" stroke-width="2" fill="none"/></svg>AwningsMirrors</li>
    <li><svg viewBox="0 0 14 14"><path d="M2 7 L6 11 L12 2" stroke="#666" stroke-width="2" fill="none"/></svg>Ceiling Fan Dusting</li>
    <li><svg viewBox="0 0 14 14"><path d="M2 7 L6 11 L12 2" stroke="#666" stroke-width="2" fill="none"/></svg>Green houses</li>
    <li><svg viewBox="0 0 14 14"><path d="M2 7 L6 11 L12 2" stroke="#666" stroke-width="2" fill="none"/></svg>Shower Enclosures</li>
    <li><svg viewBox="0 0 14 14"><path d="M2 7 L6 11 L12 2" stroke="#666" stroke-width="2" fill="none"/></svg>Construction clean up</li>
  </ul>

  <div class="abs gallery-tab">Photo Gallery</div>
  <div class="abs gallery">
    <div class="abs thumb" style="left:25px;background:linear-gradient(90deg,#7d6b5c,#a39484)" role="img" aria-label="Wooden deck before and after washing"></div>
    <div class="abs thumb" style="left:165px;background:linear-gradient(135deg,#5a3c1f,#b07a3c)" role="img" aria-label="Cleaned wooden deck floor"></div>
    <div class="abs thumb" style="left:305px;background:linear-gradient(90deg,#4a4648,#a0605a)" role="img" aria-label="Brick patio before and after pressure washing"></div>
  </div>
  <div class="abs g-arrow" style="left:28px;top:966px"><svg viewBox="0 0 26 26"><path d="M15 7 L9 13 L15 19" stroke="#fff" stroke-width="3" fill="none"/></svg></div>
  <div class="abs g-arrow" style="left:473px;top:964px"><svg viewBox="0 0 26 26"><path d="M11 7 L17 13 L11 19" stroke="#fff" stroke-width="3" fill="none"/></svg></div>

  <div class="abs certified">Quorlick`s Maintenance LLC<br>Certfied <span>By:</span></div>
  <div class="abs badge" style="left:268px;background:#3a8ed0"></div>
  <div class="abs badge" style="left:345px;background:#2f6b2a"></div>
  <div class="abs badge" style="left:422px;background:#3a8ed0"></div>

  <div class="abs card" style="top:506px">
    <div class="card-photo" role="img" aria-label="Window cleaners on ladders washing a glass storefront" style="background:linear-gradient(#1c4f9a,#7fa8d8)"></div>
    <div class="card-ribbon">Window Washing</div>
    <div class="card-body">Quorlick`s Window Cleaning offers you a professional level of service at an affordable price. We service anything from residential, small store-fronts...</div>
    <div class="card-foot"><div class="card-more">Read More</div></div>
  </div>

  <div class="abs card" style="top:713px">
    <div class="card-photo" role="img" aria-label="Water fed pole cleaning a glass building facade" style="background:linear-gradient(135deg,#1f5fa8,#9ac4ea)"></div>
    <div class="card-ribbon">Water Fed Poles</div>
    <div class="card-body">Quorlick`s uses the latest technologie in window cleaning for small buildings. No ladder, no Chemicals, no liability.Water fed pole cleaning...</div>
    <div class="card-foot"><div class="card-more">Read More</div></div>
  </div>

  <div class="abs card" style="top:924px">
    <div class="card-photo" role="img" aria-label="Customer service agent with a headset in an office" style="background:linear-gradient(90deg,#c9a88e,#e4dcd4)"></div>
    <div class="card-ribbon">Contact Us</div>
    <div class="card-body contact">
      <div class="name">Quorlick`s Maintenance LLC</div>
      P.O.Box 5520 Brindleford PA 19999<br>
      Phone:&nbsp;&nbsp; 555-014-2290<br>
      Email:&nbsp;&nbsp;&nbsp; info@quorlicks-example.com
    </div>
    <div class="card-foot"><div class="card-more">Read More</div></div>
  </div>
</div>

<div class="abs footer-info">P.O.Box 5520 Brindleford PA 19999<br>Phone: 555-014-2290&nbsp; | &nbsp;Fax: 555-014-2291<br>Email: info@quorlicks-example.com</div>
<div class="abs follow">Follow Us:<i></i><i></i><i></i><i></i></div>
<div class="abs copyright">© Copyright 2012 <b>Quorlick`s Maintenance LLC</b>. All right reserved</div>
</body>
</html>
```